Professionell und kommunikativ, kommen gerne wieder.
Zielgruppe
Wir transportieren Güter und Waren aller Art rund um die Welt. Hauptsächlich Luftfracht, aber auch per Schiff und an Land. Hauptsächlich richten wir uns damit an Firmenkunden, weniger an Privatkunden. Für unsere neue Website benötigen wir ein Design.
Aufgabenstellung
Wir benötigen ein Webdesign für den Relaunch unserer Website. Unsere Ideen für unsere neue Website haben wir bereits skizziert (Anlage). Diese Mockups bedürfen nun eines Designs.
Dazu ergänzend gelten die folgenden, formalen Vorgaben:
• 1140px breit, gerne auch Ideen für die Darstellung auf Smartphones und Tablets
• Logo links oben
• Navigation oben waagerecht
• Dropdown-Navigation am Desktop, Hamburger für die mobile Navigation
• Verwendung eines Grid-Systems wie Bootstrap
• Mindestschriftgröße für Mengentext: 16px (bei groß ausfallenden Fonts 15px)
Wir haben keine Hausschriftart und keine festgelegten Farben. Wir möchten aber unser Logo weiterverwenden und da bietet es sich natürlich an, auf dem Rot aufzubauen.

```html
<!DOCTYPE html>
<html lang="de">
<head>
<meta charset="utf-8">
<title>Skylane Cargo – We move your Business!</title>
<link href="https://fonts.googleapis.com/css2?family=Inter:wght@300;400;500;600&display=swap" rel="stylesheet">
<style>
:root{
  --red:#d90f0f;
  --ink:#141414;
  --muted:#7a7a7a;
  --line:#e6e6e6;
  --soft:#f2f2f2;
  --icon-bg:#efefef;
  --black:#000;
  --white:#fff;
}
*{box-sizing:border-box;margin:0;padding:0}
html,body{width:1200px;height:2776px;overflow:hidden;background:var(--white)}
body{font-family:'Inter',sans-serif;color:var(--ink);position:relative}
a{text-decoration:none;color:inherit}
.container{width:1000px;margin:0 auto;position:relative}

.site-header{height:88px;border-bottom:1px solid var(--line)}
.site-header .container{display:flex;align-items:center;height:87px}
.brand{font-size:23px;font-weight:300;letter-spacing:-0.5px;color:#555;display:flex;align-items:center;gap:6px}
.brand-dot{width:14px;height:14px;border-radius:50%;background:var(--red)}
.main-nav{margin-left:auto;display:flex;gap:28px;font-size:14px;color:var(--muted);margin-right:41px}
.btn{display:inline-flex;align-items:center;gap:9px;height:47px;padding:0 27px;border-radius:4px;font-size:14px;font-weight:500}
.btn-primary{background:var(--red);color:var(--white)}
.btn-outline{border:1px solid var(--red);color:var(--red);margin-right:7px}
.btn svg{width:16px;height:16px;fill:currentColor}

.hero{height:441px;text-align:center;padding-top:131px}
.hero h1{font-size:70px;font-weight:500;letter-spacing:-2px;line-height:1}
.hero p{font-size:14px;color:var(--muted);line-height:19px;margin-top:26px}
.link-more{color:var(--red);font-size:14px;font-weight:500;display:inline-flex;align-items:center;gap:8px}
.link-more svg{width:10px;height:10px;stroke:currentColor;fill:none;stroke-width:2}
.hero .link-more{margin-top:32px}

.banner{height:496px;position:relative;background:linear-gradient(90deg,#0b1320 0%,#1b2430 35%,#5a3a34 60%,#3f4a45 85%,#55605a 100%)}
.banner .container{padding-top:189px;padding-left:68px}
.accent{width:34px;height:1px;background:var(--red);display:block}
.banner h2{color:var(--white);font-size:26px;font-weight:400;margin-top:14px}
.banner .btn{margin-top:22px;height:46px;padding:0 27px}

.services{height:465px;text-align:center;padding-top:102px}
.section-title{font-size:20px;font-weight:400}
.service-grid{display:grid;grid-template-columns:repeat(4,254px);width:1016px;margin:80px auto 0}
.service-icon{width:80px;height:80px;background:var(--icon-bg);border-radius:3px;margin:0 auto;display:flex;align-items:center;justify-content:center}
.service-icon svg{width:44px;height:44px;fill:var(--red)}
.service h3{font-size:28px;font-weight:400;margin-top:36px;letter-spacing:-0.3px}
.service .link-more{margin-top:8px}

.about{height:326px;background:var(--soft);position:relative;margin-top:103px}
.about-text{position:absolute;left:100px;top:106px;width:500px}
.about-text p{font-size:17px;line-height:20px;margin-top:14px}
.about-media{position:absolute;left:693px;top:0;width:507px;height:326px;background:linear-gradient(180deg,#3b2f25 0%,#2a2a2a 30%,#8b8a6a 55%,#4a4540 80%,#6b5a48 100%)}

.partners{height:416px;text-align:center;padding-top:103px}
.partner-row{display:flex;justify-content:center;align-items:center;gap:78px;margin-top:75px}
.partner{font-size:17px;font-weight:500;display:flex;align-items:center;gap:8px}
.partner-mark{width:18px;height:18px;background:var(--ink)}

.help{height:309px;background:var(--soft);text-align:center;padding-top:67px}
.help h2{font-size:48px;font-weight:500;letter-spacing:-1px}
.help p{font-size:14px;color:var(--muted);line-height:19px;margin-top:18px}
.help .btn{margin-top:22px}

.site-footer{height:158px;background:var(--black)}
.site-footer .container{display:flex;align-items:center;justify-content:space-between;padding-top:76px}
.site-footer .brand{color:var(--white)}
.footer-link{color:var(--white);font-size:13px}
</style>
</head>
<body>

<header class="site-header">
  <div class="container">
    <a class="brand" href="#">SKYLANE CARGO <span class="brand-dot"></span></a>
    <nav class="main-nav"><a href="#">Services</a><a href="#">About</a><a href="#">Contact</a></nav>
    <a class="btn btn-outline" href="#"><svg viewBox="0 0 24 24"><path d="M6.6 10.8a15 15 0 0 0 6.6 6.6l2.2-2.2c.3-.3.7-.4 1-.2 1.1.4 2.3.6 3.6.6.6 0 1 .4 1 1V20c0 .6-.4 1-1 1A17 17 0 0 1 3 4c0-.6.4-1 1-1h3.5c.6 0 1 .4 1 1 0 1.3.2 2.5.6 3.6.1.3 0 .7-.2 1z"/></svg>Call us</a>
    <a class="btn btn-primary" href="#"><svg viewBox="0 0 24 24"><path d="M5 2h14v20H5zM8 7v2h8V7zm0 4v2h8v-2zm0 4v2h5v-2z" fill-rule="evenodd"/></svg>Get a quote</a>
  </div>
</header>

<section class="hero">
  <h1>We move your Business!</h1>
  <p>Wir gehören seit unserer Gründung einem weltweiten Agentennetz an und sind<br>dadurch in der Lage, jeden Transportauftrag für Sie zu erledigen.</p>
  <a class="link-more" href="#">See more <svg viewBox="0 0 10 10"><path d="M3 1l4 4-4 4"/></svg></a>
</section>

<section class="banner" role="img" aria-label="Photo of a red truck parked at a loading yard under a cloudy sky">
  <div class="container">
    <span class="accent"></span>
    <h2>Jetzt Frachtanfrage senden.</h2>
    <a class="btn btn-primary" href="#"><svg viewBox="0 0 24 24"><circle cx="9" cy="7" r="4"/><path d="M1 21c0-4 3.6-7 8-7s8 3 8 7z"/><path d="M17 8h6v2h-6zm0 4h6v2h-6zm0-8h6v2h-6z"/></svg>Contact</a>
  </div>
</section>

<section class="services">
  <h2 class="section-title">Our Services</h2>
  <div class="service-grid">
    <div class="service">
      <div class="service-icon"><svg viewBox="0 0 24 24"><path d="M21 16v-2l-8-5V3.5a1.5 1.5 0 0 0-3 0V9l-8 5v2l8-2.5V19l-2 1.5V22l3.5-1 3.5 1v-1.5L13 19v-5.5z"/></svg></div>
      <h3>Air Freight</h3>
      <a class="link-more" href="#">Read more <svg viewBox="0 0 10 10"><path d="M3 1l4 4-4 4"/></svg></a>
    </div>
    <div class="service">
      <div class="service-icon"><svg viewBox="0 0 24 24"><path d="M1 5h14v11H1zM16 9h4l3 4v3h-7z"/><circle cx="6" cy="18" r="2.5"/><circle cx="18.5" cy="18" r="2.5"/></svg></div>
      <h3>Land Transport</h3>
      <a class="link-more" href="#">Read more <svg viewBox="0 0 10 10"><path d="M3 1l4 4-4 4"/></svg></a>
    </div>
    <div class="service">
      <div class="service-icon"><svg viewBox="0 0 24 24"><path d="M10 1h4v3h4v6l3 1-3 7c-2 0-3-1-6-1s-4 1-6 1l-3-7 3-1V4h4zM8 6v3l4-1.3L16 9V6zM2 21c3 0 4-1.5 10-1.5S19 21 22 21v2c-3 0-4-1.5-10-1.5S5 23 2 23z"/></svg></div>
      <h3>Sea Freight</h3>
      <a class="link-more" href="#">Read more <svg viewBox="0 0 10 10"><path d="M3 1l4 4-4 4"/></svg></a>
    </div>
    <div class="service">
      <div class="service-icon"><svg viewBox="0 0 24 24"><path d="M2 19h20v2H2zM2.5 9.2l1.5-.4 2.7 2.3 5-1.3L8.2 4l2-.5 6.7 5.7 5-1.3a1.6 1.6 0 0 1 .8 3.1L5.3 15.5 2 12z"/></svg></div>
      <h3>Airline Services</h3>
      <a class="link-more" href="#">Read more <svg viewBox="0 0 10 10"><path d="M3 1l4 4-4 4"/></svg></a>
    </div>
  </div>
</section>

<section class="about">
  <div class="about-text">
    <span class="accent"></span>
    <p>The word cargo refers in particular to goods or produce being conveyed gernerally for commercial gain by ship, boat or aircraft, although the term is now often extended to cover all types of freight, including that carried by train,van, truck, or container.</p>
  </div>
  <div class="about-media" role="img" aria-label="Photo looking out of a trailer towards a forklift loading pallets at a warehouse dock"></div>
</section>

<section class="partners">
  <h2 class="section-title">Our Partners &amp; Clients</h2>
  <div class="partner-row">
    <span class="partner"><span class="partner-mark"></span>Atlantic Air</span>
    <span class="partner">Orbis Network</span>
    <span class="partner">Cedar Air</span>
  </div>
</section>

<section class="help">
  <h2>Need help?</h2>
  <p>On weekday your message will usually answered within 24 hours. We're open Monday trough<br>Friday excluding national and regional holidays. Office hours from 8 am until 4.30 pm</p>
  <a class="btn btn-primary" href="#"><svg viewBox="0 0 24 24"><path d="M3 4h3V2h2v2h8V2h2v2h3v18H3zm2 5v11h14V9zm5.5 9L7 14.5l1.4-1.4 2.1 2.1 5.1-5.1L17 11.5z"/></svg>Make a date</a>
</section>

<footer class="site-footer">
  <div class="container">
    <a class="brand" href="#">SKYLANE CARGO <span class="brand-dot"></span></a>
    <a class="footer-link" href="#">Impressum &amp; Datenschutz</a>
  </div>
</footer>

</body>
</html>
```